Heronwick Lodge Sign

Heronwick Lodge is a lake resort in Branson, MO
This resort used to have 66 units however the resort was sold in sections. I own the part of the resort that has all the amenities listed on the attached file. We need an updated sign and also billboard.
On a sign like this should be include a phone number?

```html
<!DOCTYPE html>
<html lang="en">
<head>
<meta charset="utf-8">
<title>Heronwick Lodge — Signage and Billboard</title>
<link rel="stylesheet" href="https://fonts.googleapis.com/css2?family=Poppins:wght@400;500;600;700&display=swap">
<style>
  :root {
    --page: #dcdcdc;
    --label: #6a6a6a;
    --navy: #1b3a6b;
    --lake-top: #1f4d80;
    --lake-bottom: #153868;
    --green: #6cab43;
    --white: #ffffff;
  }
  * { box-sizing: border-box; margin: 0; padding: 0; }
  html, body {
    width: 1200px; height: 1093px; overflow: hidden;
    background: var(--page);
    font-family: "Poppins", sans-serif;
  }
  .canvas { position: relative; width: 1200px; height: 1093px; }

  .panel-label {
    position: absolute;
    font-size: 12px; font-weight: 400; color: var(--label);
    letter-spacing: 0.02em;
  }

  .sign, .billboard { position: absolute; background: var(--white); overflow: hidden; }
  .sign { left: 377px; top: 100px; width: 445px; height: 557px; }
  .billboard { left: 81px; top: 737px; width: 1038px; height: 268px; }
  .backdrop { position: absolute; inset: 0; width: 100%; height: 100%; display: block; }

  .wordmark {
    position: absolute; left: 0; right: 0; text-align: center;
    color: var(--navy); font-weight: 600; letter-spacing: -0.01em; line-height: 1;
  }
  .tagline {
    position: absolute; left: 0; right: 0; text-align: center;
    color: var(--navy); font-weight: 400; line-height: 1;
  }

  .amenities-title {
    position: absolute; color: var(--green); font-weight: 600;
    text-transform: uppercase; line-height: 1;
  }
  .amenity-list {
    position: absolute; list-style: none;
    color: var(--white); font-weight: 600; line-height: 1;
  }
  .amenity-list li { position: relative; white-space: nowrap; }
  .amenity-list li::before {
    content: ""; position: absolute;
    width: 4px; height: 8px;
    border-right: 2.2px solid var(--green);
    border-bottom: 2.2px solid var(--green);
    transform: rotate(45deg);
  }

  .phone { position: absolute; color: var(--green); font-weight: 700; line-height: 1; letter-spacing: -0.02em; }
  .website { position: absolute; color: var(--navy); font-weight: 700; line-height: 1; }
  .contact-line { position: absolute; color: var(--navy); font-weight: 600; line-height: 1; white-space: nowrap; }
  .contact-line .divider { color: var(--green); padding: 0 5px; font-weight: 400; }

  /* Signage placements */
  .sign .wordmark { top: 72px; font-size: 36px; }
  .sign .tagline { top: 122px; font-size: 20px; }
  .sign .amenities-title { left: 36px; top: 224px; font-size: 19px; letter-spacing: 0.14em; }
  .sign .amenity-list { top: 260px; font-size: 11.8px; }
  .sign .amenity-list li { height: 17.9px; }
  .sign .amenity-list li::before { left: -17px; top: -1px; }
  .sign .col-a { left: 56px; }
  .sign .col-b { left: 231px; }
  .sign .phone { left: 36px; top: 461px; font-size: 28px; }
  .sign .website { left: 36px; top: 492px; font-size: 17.5px; }
  .sign .contact-line { left: 36px; top: 514px; font-size: 15.5px; }

  /* Billboard placements */
  .billboard .brand-block { position: absolute; left: 30px; width: 310px; top: 0; height: 268px; }
  .billboard .wordmark { top: 100px; font-size: 34px; }
  .billboard .tagline { top: 142px; font-size: 19.5px; }
  .billboard .phone { left: 0; right: 0; text-align: center; top: 180px; font-size: 36px; }
  .billboard .website { left: 0; right: 0; text-align: center; top: 217px; font-size: 20px; }
  .billboard .amenities-title { left: 452px; top: 46px; font-size: 25px; letter-spacing: 0.48em; }
  .billboard .amenity-list { top: 82px; font-size: 12.4px; }
  .billboard .amenity-list li { height: 19.6px; }
  .billboard .amenity-list li::before { left: -13px; top: -1px; }
  .billboard .col-a { left: 471px; }
  .billboard .col-b { left: 622px; }
  .billboard .col-c { left: 838px; }
  .billboard .address-block {
    position: absolute; left: 740px; width: 236px; top: 206px;
    text-align: center; color: var(--white); font-weight: 700;
    font-size: 20px; line-height: 1.05;
  }
</style>
</head>
<body>
<main class="canvas">

  <p class="panel-label" style="left:378px; top:73px;">SIGNAGE</p>

  <section class="sign" aria-label="Resort signage">
    <svg class="backdrop" viewBox="0 0 748 936" preserveAspectRatio="none">
      <defs>
        <linearGradient id="lakeSign" x1="0" y1="0" x2="0" y2="1">
          <stop offset="0" stop-color="var(--lake-bottom)"/>
          <stop offset="0.45" stop-color="var(--lake-top)"/>
          <stop offset="1" stop-color="var(--lake-bottom)"/>
        </linearGradient>
      </defs>
      <path fill="var(--green)" d="M0,305 C70,270 170,275 260,318 C350,358 460,378 560,376 C650,374 710,360 748,345 L748,356 C710,366 650,376 560,377 C460,379 350,362 260,332 C170,302 70,302 0,336 Z"/>
      <path fill="var(--green)" d="M300,712 C420,740 520,820 640,822 C700,823 730,812 748,800 L748,786 C720,798 690,804 640,802 C540,800 440,735 330,712 Z"/>
      <g role="img" aria-label="Lakeside photo of a dock and open water, tinted deep blue">
        <path fill="url(#lakeSign)" d="M0,336 C70,302 170,302 260,332 C350,362 460,379 560,377 C650,376 710,366 748,356 L748,786 C720,798 690,804 640,802 C540,800 440,735 330,712 C240,700 120,712 0,752 Z"/>
      </g>
      <path fill="none" stroke="var(--green)" stroke-width="4" d="M0,918 C120,906 250,922 374,914 C500,906 620,922 748,912"/>
      <path fill="var(--navy)" d="M0,926 C120,916 250,930 374,924 C500,916 620,930 748,922 L748,936 L0,936 Z"/>
    </svg>

    <h1 class="wordmark">Heronwick Lodge</h1>
    <p class="tagline">on Table Rock Lake</p>

    <h2 class="amenities-title">Amenities</h2>
    <ul class="amenity-list col-a">
      <li>Direct Lake Access</li>
      <li>Swim Decks</li>
      <li>Slip Rentals</li>
      <li>Boat Rentals</li>
      <li>Indoor Pool</li>
      <li>Golf Carts</li>
      <li>Pontoon Boats</li>
      <li>Kayak-Paddleboard</li>
    </ul>
    <ul class="amenity-list col-b">
      <li>1-3 Bedroom Vacation Rentals</li>
      <li>Dining Hall</li>
      <li>Game Room</li>
      <li>Children’s Activities</li>
      <li>Pet Friendly</li>
      <li>Gift Store</li>
      <li>Outdoor Games</li>
      <li>Family Reunions-Large Group</li>
    </ul>

    <p class="phone">1.800.555.0142</p>
    <p class="website">HeronwickLodge.com</p>
    <p class="contact-line">28 Willow Bend Lane<span class="divider">|</span>info@heronwicklodge.com</p>
  </section>

  <p class="panel-label" style="left:88px; top:709px;">BILLBOARD</p>

  <section class="billboard" aria-label="Resort billboard">
    <svg class="backdrop" viewBox="0 0 1744 450" preserveAspectRatio="none">
      <defs>
        <linearGradient id="lakeBoard" x1="0" y1="0" x2="0" y2="1">
          <stop offset="0" stop-color="var(--lake-bottom)"/>
          <stop offset="0.5" stop-color="var(--lake-top)"/>
          <stop offset="1" stop-color="var(--lake-bottom)"/>
        </linearGradient>
      </defs>
      <path fill="var(--green)" d="M664,0 C640,70 672,112 700,155 C732,212 722,292 668,340 C610,395 555,428 505,450 L1744,450 L1744,0 Z"/>
      <g role="img" aria-label="Lakeside photo of a dock and open water, tinted deep blue">
        <path fill="url(#lakeBoard)" d="M684,0 C664,62 694,104 720,150 C752,212 738,294 684,342 C624,398 564,430 512,450 L1744,450 L1744,0 Z"/>
      </g>
      <path fill="var(--green)" d="M1060,450 C1110,380 1200,320 1330,325 C1450,330 1560,330 1650,310 C1700,298 1730,280 1744,255 L1744,450 Z"/>
    </svg>

    <div class="brand-block">
      <h1 class="wordmark">Heronwick Lodge</h1>
      <p class="tagline">on Table Rock Lake</p>
      <p class="phone">1.800.555.0142</p>
      <p class="website">HeronwickLodge.com</p>
    </div>

    <h2 class="amenities-title">Amenities</h2>
    <ul class="amenity-list col-a">
      <li>Direct Lake Access</li>
      <li>Swim Decks</li>
      <li>Slip Rentals</li>
      <li>Boat Rentals</li>
      <li>Indoor Pool</li>
      <li>Golf Carts</li>
      <li>Pontoon Boats</li>
    </ul>
    <ul class="amenity-list col-b">
      <li>Kayak-Paddleboard</li>
      <li>1-3 Bedroom Vacation Rentals</li>
      <li>Dining Hall</li>
      <li>Game Room</li>
      <li>Children’s Activities</li>
    </ul>
    <ul class="amenity-list col-c">
      <li>Pet Friendly</li>
      <li>Gift Store</li>
      <li>Outdoor Games</li>
      <li>Family Reunions-Large Group</li>
    </ul>

    <p class="address-block">28 Willow Bend Lane<br>info@heronwicklodge.com</p>
  </section>

</main>
</body>
</html>
```